Commercial wall and ceiling contractor needs website

Construction trade companies are notoriously behind the rest of the world when it comes to using current technology to run their businesses; we are not one of those companies. We are a walls and ceilings contractor using up to date communications technologies and applying them unlike any other in our trade. As simple as it sounds, and it really is that simple, it is still a new idea in the trade. We are moving our customers towards communicating with us through a single point of contact using text and email; we distribute information to the appropriate internal party on our end. We need a website that generally appears traditionally familiar to the visitor while also expresses a fresh new approach and edginess to the trade business.

Target Market(s)

General contractors looking to get a bit of background info before inviting us to bid on their projects. This is not a high traffic environment. Their subsequent site visits will be primarily for contact info.

Industry/Entity Type

Construction Company

Number of Pages Required

3 page

Font styles to use
Sans Serif

Requirements
Must have
• The file I uploaded named "plomsite.docx" does not have to appear on the site in the same manner in which appears in the document file; but the info contained within that document does need to be represented on the site.

```html
<!DOCTYPE html>
<html lang="en">
<head>
<meta charset="utf-8">
<title>Norvale Walls &amp; Ceilings</title>
<link href="https://fonts.googleapis.com/css2?family=Lato:wght@400;700;900&display=swap" rel="stylesheet">
<style>
:root{
  --green:#1b5a38;
  --gold:#b0761f;
  --gold-soft:#ead9bd;
  --ink:#1d1d1d;
  --cream:#f9f6f1;
  --line:#d9d9d9;
  --white:#fff;
}
*{box-sizing:border-box;margin:0;padding:0}
html,body{width:1200px;height:2919px;overflow:hidden}
body{font-family:'Lato',sans-serif;color:var(--ink);background:var(--white);position:relative}
a{color:inherit;text-decoration:none}
.abs{position:absolute}
.btn{position:absolute;display:flex;align-items:center;justify-content:center;font-weight:700;font-size:15px;text-transform:uppercase;letter-spacing:.2px}
.btn-gold{background:var(--gold);color:var(--white)}
.btn-white{background:var(--white);color:var(--green)}
.btn-outline{border:2px solid var(--ink);color:var(--ink)}
.btn-outline-light{border:2px solid var(--white);color:var(--white)}

/* header */
.brand{left:117px;top:18px;display:flex;align-items:center;gap:10px;font-weight:900;font-size:20px;color:var(--gold);letter-spacing:1px}
.brand-mark{width:22px;height:22px;border:3px solid var(--green)}
.topbar{left:420px;top:12px;font-size:11px;display:flex;gap:22px;color:var(--ink)}
.topbar b{font-weight:900;margin-right:4px}
.nav{left:386px;top:51px;display:flex;gap:43px;font-size:15px}
.nav .active{color:var(--green)}

/* hero */
.hero{left:0;top:86px;width:1200px;height:495px;background:linear-gradient(180deg,#8c8c8c 0%,#5d5a55 45%,#3e3b38 100%);border:1px solid var(--gold)}
.hero-shade{position:absolute;inset:0;background:rgba(0,0,0,.25)}
.hero h1{position:absolute;left:0;width:1200px;top:120px;text-align:center;color:var(--white);font-weight:900;font-size:52px;line-height:50px;text-transform:uppercase}
.hero p{position:absolute;left:0;width:1200px;top:233px;text-align:center;color:var(--white);font-size:20px;line-height:30px}

/* about */
.about-photo{left:117px;top:652px;width:510px;height:277px;background:linear-gradient(135deg,#cfd3d6,#8e959a 60%,#d7c545)}
.section-title{color:var(--green);font-weight:900;text-transform:uppercase}
.about-title{left:668px;top:650px;font-size:42px;line-height:40px}
.about-text{left:668px;top:738px;width:370px;font-size:20px;line-height:30px}
.stat{position:absolute;top:972px;width:135px;height:176px;background:var(--white);box-shadow:0 2px 8px rgba(0,0,0,.1);text-align:center}
.stat svg{position:absolute;left:39px;top:18px}
.stat-num{position:absolute;top:88px;width:100%;font-size:40px;font-weight:900;color:var(--gold)}
.stat-label{position:absolute;top:140px;width:100%;font-size:11px}

/* values */
.values{left:0;top:1228px;width:1200px;height:511px;background:var(--cream)}
.values-title{position:absolute;width:100%;top:78px;text-align:center;font-size:42px}
.value{position:absolute;top:183px;width:276px;text-align:center}
.value-art{width:112px;height:112px;margin:0 auto;background:var(--gold-soft);border-radius:6px}
.value h3{margin-top:20px;font-size:22px;line-height:26px;font-weight:700}
.value p{margin-top:8px;font-size:16px;line-height:22px}

/* services */
.services-title{left:0;top:1818px;width:1200px;text-align:center;font-size:42px}
.service{position:absolute;top:1914px;width:232px;height:259px;background:var(--white);box-shadow:0 2px 8px rgba(0,0,0,.1)}
.service-photo{height:165px}
.service h4{height:94px;display:flex;align-items:center;justify-content:center;text-align:center;font-size:16px;font-weight:700;line-height:22px}
.service.featured{background:var(--gold);color:var(--white)}

/* band */
.band{left:0;top:2253px;width:1200px;height:145px;background:var(--green)}
.band p{position:absolute;left:213px;top:56px;color:var(--white);font-size:24px}

/* footer */
.foot-title{font-size:20px;font-weight:700;color:var(--green)}
.quick{left:117px;top:2490px}
.quick ul{list-style:none;margin-top:22px}
.quick li{font-size:15px;line-height:29px}
.connect{left:322px;top:2490px;width:440px}
.field{position:absolute;font-size:11px;border-bottom:1px solid var(--line);padding-bottom:11px}
.touch{left:832px;top:2490px;font-size:15px;line-height:22px}
.rule{left:117px;top:2829px;width:966px;height:1px;background:var(--line)}
.copy{left:0;top:2858px;width:1200px;text-align:center;font-size:15px}
</style>
</head>
<body>

<header>
  <a class="abs brand" href="#"><span class="brand-mark"></span>NORVALE</a>
  <div class="abs topbar">
    <span><b>OFFICE</b>Monday-Friday 08:00-16:30 Pacific</span>
    <span><b>TEXT</b>555-210-4830</span>
    <span><b>EMAIL</b>hello@norvaleinteriors.example</span>
  </div>
  <nav class="abs nav">
    <a class="active" href="#">Home</a><a href="#">About Us</a><a href="#">Services</a><a href="#">Projects</a><a href="#">Contact Us</a>
  </nav>
  <a class="btn btn-gold" href="#" style="left:866px;top:41px;width:217px;height:44px">Request a Budget</a>
</header>

<section class="abs hero" role="img" aria-label="Open-plan office interior with cubicles and a finished ceiling">
  <div class="hero-shade"></div>
  <h1>We are a walls and<br>ceilings contractor</h1>
  <p>Using up to date communications technologies and<br>applying them unlike any other in our trade.</p>
  <a class="btn btn-gold" href="#" style="left:386px;top:336px;width:218px;height:44px">Request a Budget</a>
  <a class="btn btn-white" href="#" style="left:614px;top:336px;width:218px;height:44px">Contact Us</a>
</section>

<section>
  <div class="abs about-photo" role="img" aria-label="Worker in hard hat and safety vest installing a ceiling vent"></div>
  <h2 class="abs section-title about-title">About<br>Company</h2>
  <p class="abs about-text">We are a walls and ceilings contractor using up to date communications technologies and applying them unlike any other in our trade.</p>
  <a class="btn btn-outline" href="#" style="left:668px;top:883px;width:135px;height:44px">Learn More</a>

  <div class="stat" style="left:185px">
    <svg width="58" height="50" viewBox="0 0 58 50" fill="none" stroke="#c9a77a" stroke-width="2"><rect x="2" y="12" width="54" height="36" rx="3"/><path d="M20 12V5h18v7M2 26h54"/><rect x="25" y="22" width="8" height="8"/></svg>
    <div class="stat-num">25</div><div class="stat-label">Years in Business</div>
  </div>
  <div class="stat" style="left:355px">
    <svg width="58" height="56" viewBox="0 0 58 56" fill="none" stroke="#c9a77a" stroke-width="2"><path d="M8 46V10h36M36 4l8 6-8 6M50 10v36H14M22 52l-8-6 8-6"/></svg>
    <div class="stat-num">92%</div><div class="stat-label">Repeat Clients</div>
  </div>
  <div class="stat" style="left:525px">
    <svg width="58" height="58" viewBox="0 0 58 58" fill="none" stroke="#c9a77a" stroke-width="2"><circle cx="29" cy="29" r="27"/><path d="M20 30l6 6 12-13"/></svg>
    <div class="stat-num">900</div><div class="stat-label">Projects Completed</div>
  </div>
  <div class="stat" style="left:695px">
    <svg width="58" height="58" viewBox="0 0 58 58" fill="none" stroke="#c9a77a" stroke-width="2"><path d="M10 20h8v20h-8zM18 22l10-16c4 0 5 3 4 6l-2 8h12c3 0 4 3 3 5l-4 13H18"/><path d="M6 50l2 5 2-5-4-2h6zM24 50l2 5 2-5-4-2h6zM42 50l2 5 2-5-4-2h6z"/></svg>
    <div class="stat-num">95%</div><div class="stat-label">COR Rating (2018)</div>
  </div>
  <div class="stat" style="left:865px">
    <svg width="58" height="50" viewBox="0 0 58 50" fill="none" stroke="#c9a77a" stroke-width="2"><circle cx="29" cy="10" r="7"/><circle cx="12" cy="16" r="5"/><circle cx="46" cy="16" r="5"/><path d="M17 46c0-14 4-22 12-22s12 8 12 22zM4 38c0-10 3-14 8-14M54 38c0-10-3-14-8-14"/></svg>
    <div class="stat-num">150</div><div class="stat-label">Team Members</div>
  </div>
</section>

<section class="abs values">
  <h2 class="section-title values-title">Our Values</h2>
  <div class="value" style="left:136px">
    <div class="value-art" role="img" aria-label="Line illustration of a handshake forming a heart"></div>
    <h3>Relationships</h3>
    <p>We develop strong relationships with our employees and families, our community, and our clients. These relationships create customers for life.</p>
  </div>
  <div class="value" style="left:462px">
    <div class="value-art" role="img" aria-label="Line illustration of two hands holding a heart with a tick"></div>
    <h3>Honesty &amp; Integrity</h3>
    <p>For more than 25 years, our trusted relationships have been built on honesty and integrity. We say what we mean, and we do what we say.</p>
  </div>
  <div class="value" style="left:789px">
    <div class="value-art" role="img" aria-label="Line illustration of a building blueprint scroll"></div>
    <h3>What Makes Us Unique</h3>
    <p>We solve our customer’s problems by listening to their challenges and delivering high quality, innovative solutions that work.</p>
  </div>
</section>

<section>
  <h2 class="abs section-title services-title">What We Do</h2>
  <div class="service" style="left:117px">
    <div class="service-photo" role="img" aria-label="Curved wooden lattice specialty ceiling" style="background:linear-gradient(135deg,#f1d6a3,#c8934f 60%,#7a5030)"></div>
    <h4>Specialty Ceiling<br>Panels</h4>
  </div>
  <div class="service featured" style="left:361px">
    <div class="service-photo" role="img" aria-label="White T-bar ceiling grid" style="background:linear-gradient(135deg,#f4f4f4,#d8d8d8)"></div>
    <h4>T-Bar Ceiling<br>Panels &amp; Installation</h4>
  </div>
  <div class="service" style="left:606px">
    <div class="service-photo" role="img" aria-label="Metal ceiling structure with skylight and pendant lamp" style="background:linear-gradient(135deg,#8fb6d8,#3f6f99 60%,#6b7b88)"></div>
    <h4>Metal Ceiling<br>Panels &amp; Installation</h4>
  </div>
  <div class="service" style="left:851px">
    <div class="service-photo" role="img" aria-label="Red plastered corridor ceiling with downlights" style="background:linear-gradient(180deg,#a3271c,#7e1f16 55%,#cfa983)"></div>
    <h4>Commercial Drywall<br>Taping &amp; Plastering</h4>
  </div>
</section>

<section class="abs band">
  <p>Trust the team with over 25 years of experience</p>
  <a class="btn btn-outline-light" href="#" style="left:769px;top:50px;width:218px;height:44px">Request a Budget</a>
</section>

<footer>
  <div class="abs quick">
    <h3 class="foot-title">Quick links</h3>
    <ul><li>About Us</li><li>Our Services</li><li>Design Assist</li><li>Completed Projects</li><li>Contact Us</li><li>Request A Budget</li></ul>
  </div>
  <div class="abs connect">
    <h3 class="foot-title">Connect With Us</h3>
    <div class="field" style="left:0;top:52px;width:215px">Name</div>
    <div class="field" style="left:225px;top:52px;width:215px">Email</div>
    <div class="field" style="left:0;top:98px;width:215px">Phone</div>
    <div class="field" style="left:225px;top:98px;width:215px">Select Service</div>
    <div class="field" style="left:0;top:142px;width:440px;height:60px">Message here...</div>
    <a class="btn btn-gold" href="#" style="left:0;top:224px;width:129px;height:44px">Submit</a>
  </div>
  <div class="abs touch">
    <h3 class="foot-title">Get In Touch.</h3>
    <p style="margin-top:18px;font-weight:700">Norvale Walls &amp; Ceilings.</p>
    <p style="margin-top:12px">1180 Cedar Row, Millbrook,<br>BC, V0X 1A0</p>
    <p style="margin-top:14px">555-210-4830<br>hello@norvaleinteriors.example</p>
  </div>
  <div class="abs rule"></div>
  <p class="abs copy">Copyright © 2019 Norvale Walls &amp; Ceilings.&nbsp; All rights reserved.</p>
</footer>

</body>
</html>
```